Book Cover Design Project

I have written a booK called "Build From Nothing:
a handbook for launching and steering a modest enterprise. It is aimed at the start up entrepreneur and seeks to give them everything they need to start up and run a small business. I am interested in a very simple cover that is contemporary in the look but clearly communicates the mission of the book. It should sell very well as there are no others like it, so the designer will get excellent exposure.
Updates

Reason: I an vacation in Europe until the 23rd of July. Would like a few days to make a decision after my return Ned

We are currently on vacation.  Will make a final decision in about a week.  Thanks so much for your submissions

Ned

Target Market(s)

Start up businesses in the U.S.

Industry/Entity Type

Business

Requirements
Must have
• Clear communication of the name. Lots of white space. Graphic communication of the purpose of the book? Prominent exposure of my name. Edward r. Kistlewood

```html
<!DOCTYPE html>
<html lang="en">
<head>
<meta charset="utf-8">
<title>Build From Nothing – Edward R. Kistlewood</title>
<link rel="stylesheet" href="https://fonts.googleapis.com/css2?family=Oswald:wght@400;500;600&family=Montserrat:wght@800&display=swap">
<style>
  :root {
    --paper: #ffffff;
    --ink: #000000;
    --forest: #10600f;
    --forest-dark: #0b4d0b;
    --stone: #d8d8d8;
    --stone-dark: #6a6a6a;
  }
  * { margin: 0; padding: 0; box-sizing: border-box; }
  html, body {
    width: 800px;
    height: 1200px;
    overflow: hidden;
    background: var(--paper);
  }
  .cover {
    position: relative;
    width: 800px;
    height: 1200px;
    background: var(--paper);
    overflow: hidden;
  }
  .cover-art {
    position: absolute;
    inset: 0;
    width: 800px;
    height: 1200px;
  }
  .title-line {
    font-family: "Oswald", sans-serif;
    font-weight: 600;
    fill: var(--ink);
    stroke: var(--forest);
    stroke-width: 3;
    paint-order: stroke;
    filter: drop-shadow(4px 4px 0 var(--forest-dark));
  }
  .subtitle-line {
    font-family: "Oswald", sans-serif;
    font-weight: 400;
    fill: var(--ink);
  }
  .subtitle-emphasis {
    font-family: "Oswald", sans-serif;
    font-weight: 600;
    fill: var(--forest);
    filter: drop-shadow(3px 3px 0 var(--ink));
  }
  .author-name {
    font-family: "Montserrat", sans-serif;
    font-weight: 800;
    fill: var(--forest);
  }
  .progress-arrow-outline { fill: none; stroke: var(--ink); stroke-width: 9; stroke-linejoin: miter; }
  .progress-arrow-fill { fill: none; stroke: var(--paper); stroke-width: 5; stroke-linejoin: miter; }
  .footer-band { fill: var(--forest); }

  .illustration-thumbs-up {
    position: absolute;
    left: 0;
    top: 684px;
    width: 218px;
    height: 232px;
    border-radius: 0 50% 50% 0 / 0 50% 50% 0;
    background: radial-gradient(circle at 45% 55%, var(--stone) 0%, var(--forest) 70%, var(--stone-dark) 100%);
  }
  .illustration-pointing-hand {
    position: absolute;
    right: 0;
    top: 0;
    width: 164px;
    height: 120px;
    background: linear-gradient(135deg, var(--stone) 0%, var(--paper) 45%, var(--forest) 100%);
    border-bottom-left-radius: 60px;
  }
</style>
</head>
<body>
<main class="cover">
  <svg class="cover-art" viewBox="0 0 800 1200" xmlns="http://www.w3.org/2000/svg">
    <g class="book-title">
      <text class="title-line" x="222" y="284" font-size="268" textLength="362" lengthAdjust="spacingAndGlyphs">BUILD</text>
      <text class="title-line" x="222" y="529" font-size="275" textLength="362" lengthAdjust="spacingAndGlyphs">FROM</text>
      <text class="title-line" x="222" y="698" font-size="180" textLength="362" lengthAdjust="spacingAndGlyphs">NOTHING:</text>
    </g>

    <g class="progress-arrow">
      <polyline class="progress-arrow-outline" points="150,768 189,712 652,712"/>
      <polygon points="644,698 662,712 644,726" fill="var(--paper)" stroke="var(--ink)" stroke-width="2.5"/>
      <polyline class="progress-arrow-fill" points="150,768 189,712 648,712"/>
    </g>

    <g class="book-subtitle" text-anchor="end">
      <text class="subtitle-line" x="662" y="792" font-size="58" textLength="420" lengthAdjust="spacingAndGlyphs">a handbook for launching</text>
      <text class="subtitle-line" x="662" y="856" font-size="58">and steering a</text>
      <text class="subtitle-emphasis" x="662" y="920" font-size="58" textLength="410" lengthAdjust="spacingAndGlyphs">MODEST ENTERPRISE</text>
    </g>

    <text class="author-name" x="111" y="1090" font-size="52" textLength="578" lengthAdjust="spacingAndGlyphs">EDWARD R. KISTLEWOOD</text>
    <rect class="footer-band" x="0" y="1085" width="800" height="115"/>
  </svg>

  <div class="illustration-thumbs-up" role="img" aria-label="Illustration of a thumbs-up hand bursting out of a key and globe emblem"></div>
  <div class="illustration-pointing-hand" role="img" aria-label="Illustration of a cartoon pointing hand emerging from a peeled page corner"></div>
</main>
</body>
</html>
```